Basketball Training Facility Flyer Design

We need a killer flyer designed for our brand new state of the art basketball training facility here in Syracuse, Utah. This flyer will be distributed to coaches, parents and players in a large school district in Davis and Weber county, Utah. The purpose of the flyer is to announce the launch of the new facility and to encourage parents, coaches and players to come and try out the facility for a free initial session. We're offering a completely complimentary first training session to introduce customers to the facility at no cost.

We use technology and equipment that is typically found in PLH-level training facilities and gymnasiums. Our website can be found here for some additional information - www.corvanhoopworks.com. Customers can easily book and pay online through our website (the functionality will be done by the time we distribute the completed flyer).

The design needs to highlight the equipment we offer at the facility, because no other basketball training center has the same level of technology we do. We want the flyer to be clean and simple.

Please see must haves for specific details.

The size of the flyer we want to print is 5.75 inches by 9.5 inches.

Target Market(s)

Parents of basketball players of all skill levels age 8-18.

Industry/Entity Type

Training

Requirements
Must have
• Design must include this header: You want to dominate on the court. We have the formula to make that happen.

Design must include this sub header or highlight: Free Introductory Training Session!

The design must include our Logo

The design must include the photos attached of the Rebo, the Jumplora and the Dribtek

Under the the photo of the Rebo 4200 (attached) please include this verbiage:
Game Shots in Game Spots at Game Speed

Under the photo of the Jumplora (see attached) please include this verbiage:
Improve Power, Agility and Speed like Never Before

Under the photo of the Dribtek (attached) please include this verbiage:
Real Time Statistics to Improve Dribble Speed, Accuracy and Right / Left Comparison

Include this verbiage somewhere in the design: Technology Used by PLH and the Best D-1 College Teams

The design must include a strong call to action: Call or Click Now to Schedule A Free Training Session!

The design must include our contact information in easy-to-read font and size (also specifically highlighting the website):

Schedule Online in Less Than 60 Seconds!
Call or Click
801-482-7195
www.corvanhoopworks.com
Nice to have
• For examples of the type of design we like, please see the attached images labeled

Please use stock photos of your preference to go in the flyer (preferably images of youth basketball training or kids in basketball training)

We don't want the flyer to be too cluttered, so please use images at your discretion.

Thank you!

```html
<!DOCTYPE html>
<html lang="en">
<head>
<meta charset="utf-8">
<title>Corvan Hoopworks – Free Introductory Training Session</title>
<link href="https://fonts.googleapis.com/css2?family=Archivo:ital,wght@1,900&family=Arvo:wght@400;700&family=Mulish:ital,wght@0,400;0,700;0,800;1,400;1,800&display=swap" rel="stylesheet">
<style>
  :root {
    --panel: #231f20;
    --page: #f5f5f5;
    --white: #ffffff;
    --yellow: #f2e84b;
    --orange: #e7822d;
    --shadow: #000000;
    --dash: #d8d8d8;
    --logo-ring: #c4471c;
    --logo-fill: #8a2c10;
  }
  * { margin: 0; padding: 0; box-sizing: border-box; }
  html, body { width: 782px; height: 1200px; overflow: hidden; background: var(--page); }
  .flyer {
    position: relative; width: 728px; height: 1200px;
    background: var(--panel); color: var(--white); overflow: hidden;
    font-family: "Mulish", sans-serif;
  }
  .abs { position: absolute; }

  .brand-mark {
    left: 46px; top: 30px; width: 190px; height: 190px; border-radius: 50%;
    background: var(--logo-fill); border: 6px solid var(--logo-ring);
    display: flex; align-items: center; justify-content: center; text-align: center;
  }
  .brand-mark span {
    font-family: "Arvo", serif; font-weight: 700; font-size: 22px; line-height: 1.15; color: var(--white);
  }
  .watermark {
    left: 330px; top: 790px; width: 420px; height: 420px; border-radius: 50%;
    border: 26px solid rgba(255,255,255,0.04);
  }

  .title {
    left: 306px; top: 50px; width: 400px;
    font-family: "Archivo", sans-serif; font-style: italic; font-weight: 900;
    font-size: 66px; line-height: 84px; text-align: center;
    text-shadow: 5px 6px 0 var(--shadow);
  }

  .headline { font-family: "Arvo", serif; font-weight: 700; }
  .headline .lead { left: 12px; top: 308px; font-size: 31px; }
  .headline .big { left: 266px; top: 282px; font-size: 92px; color: var(--yellow); letter-spacing: -1px; }
  .headline .tail { right: 10px; top: 376px; font-size: 33px; }

  .formula { left: 12px; top: 428px; font-size: 30px; font-style: italic; color: var(--yellow); white-space: nowrap; }
  .formula b { font-weight: 800; font-size: 36px; color: var(--white); }

  .offer { left: 0; width: 728px; top: 512px; text-align: center; font-size: 31px; color: var(--orange); }

  .why { left: 73px; top: 590px; font-size: 23px; }
  .proof { left: 253px; top: 593px; font-size: 11px; line-height: 16px; }
  .formula-line { left: 73px; top: 622px; font-size: 23px; font-style: italic; color: var(--yellow); }

  .photo { border-radius: 40% 50% 45% 50%; }
  .photo-rebo { left: 280px; top: 668px; width: 110px; height: 128px;
    background: radial-gradient(ellipse at center, #c9c9c9 0%, #a33 40%, rgba(80,80,80,0.3) 75%, transparent 100%); }
  .photo-jumplora { left: 26px; top: 786px; width: 170px; height: 160px;
    background: radial-gradient(ellipse at 50% 60%, #3a6fb0 0%, #4a4a4a 55%, transparent 100%); }
  .photo-dribtek { left: 250px; top: 968px; width: 160px; height: 118px;
    background: radial-gradient(ellipse at 40% 50%, #c0612a 0%, #8a3d1c 45%, rgba(60,60,60,0.4) 75%, transparent 100%); }

  .caption { font-size: 14px; line-height: 19px; font-style: italic; }
  .cap-power { left: 133px; top: 698px; }
  .cap-shots { left: 218px; top: 826px; }
  .cap-sensors { left: 52px; top: 972px; }

  .services {
    left: 415px; top: 712px; width: 284px; height: 235px;
    border: 2px dashed var(--dash); padding: 6px 10px;
    font-family: "Arvo", serif; font-size: 20px; line-height: 28px;
  }
  .services li { list-style: none; border-bottom: 2px dashed var(--dash); padding: 1px 0 2px; }
  .services li:last-child { border-bottom: none; }
  .services .hot { color: var(--yellow); font-weight: 700; }

  .contact { left: 430px; top: 966px; width: 290px; font-size: 13px; line-height: 17px; }
  .contact .cta { color: var(--yellow); font-weight: 800; margin-bottom: 5px; }
  .contact .phone { margin-top: 6px; }
  .contact .web { color: var(--yellow); font-style: italic; font-size: 17px; margin-top: 3px; }
</style>
</head>
<body>
<main class="flyer">
  <div class="abs watermark" aria-hidden="true"></div>

  <div class="abs brand-mark"><span>Corvan<br>Hoopworks</span></div>
  <h1 class="abs title">Corvan<br>Hoopworks</h1>

  <div class="headline">
    <p class="abs lead">You want to</p>
    <p class="abs big">dominate</p>
    <p class="abs tail">on the court.</p>
  </div>
  <p class="abs formula">We have the <b>formula</b> to make that happen.</p>

  <h2 class="abs offer">Free Introductory Training Session!</h2>

  <p class="abs why">Find out why</p>
  <p class="abs proof">Technology Used by PLH and the Best D-1 College Teams<br>The Only Basketball Training Facility of its Kind in Utah</p>
  <p class="abs formula-line">Superior Technology = Superior Training</p>

  <div class="abs photo photo-rebo" role="img" aria-label="Rebo 4200 shooting machine with net and hoop"></div>
  <div class="abs photo photo-jumplora" role="img" aria-label="Young player training on the Jumplora resistance platform"></div>
  <div class="abs photo photo-dribtek" role="img" aria-label="Dribtek sensor basketball beside a smartphone showing stats"></div>

  <p class="abs caption cap-power">Improve Power,<br>Agility and Speed<br>like Never Before</p>
  <p class="abs caption cap-shots">Game Shots<br>in Game Spots<br>at Game Speed</p>
  <p class="abs caption cap-sensors">Basketball Sensors with Real<br>Time Statistics to Improve<br>Dribble Speed, Accuracy<br>and Right / Left Comparison</p>

  <ul class="abs services">
    <li>One on One /<br>Individual Sessions</li>
    <li><span class="hot">Group Sessions</span><br>(2-5 players with<br>discounts applying)</li>
    <li>Team Training</li>
    <li>Monthly Memberships</li>
  </ul>

  <div class="abs contact">
    <p class="cta">Call or Click Now to<br>Schedule A Free Training Session!</p>
    <p>Schedule Online in Less Than 60 Seconds!<br>Call or Click</p>
    <p class="phone">801-482-7195</p>
    <p class="web">www.corvanhoopworks.com</p>
  </div>
</main>
</body>
</html>
```